Craft beer central! New brew pub needs website that doesn't suck.

We are a new brewpub in Picton, Ontario. We have a kitchen and are about to start with our own beer. Currently I have a really horrid horrid website.

Check it out www.thebriarwoodtavern.example (please don't laugh too hard)

I'm on Facebook as well which might give a better idea of who we are
(it's my main social media)
https://www.facebook.com/millstonelanetavern

(there is a long story with the name difference)

I want something that I can edit myself (things like events, dates,etc), change the menu pdf, add events, have a contact page, have a gallery of pics, our beer/wine menu and eventually what we are putting on tap ourselves.

We currently have 16 craft beers on tap, local wine and our tag line is "taste the treasures of the hollow".
Updates

Project Deadline Extended
Reason: Sorry to have extended it. Have a few things on this week. Cheers,

Target Market(s)

craft beer, tourists.

Industry/Entity Type

Hospitality

Number of Pages Required

4 page

Font styles to use
Other font styles liked:
• Museo slab and next bold.

Requirements
Must have
• Must be able to attach a menu pdf (I have a food menu and beer/wine menu)
• Must have an events page so I can edit/ add them as we go on
• contacts page
• Must have a gallery that I can edit/swap pictures.
Nice to have
• Modern, hip looking page. Love black, white, grey and a splash of red.
Should not have
• be a feminine looking site. look at our Facebook page to look at our decor.

```html
<!DOCTYPE html>
<html lang="en">
<head>
<meta charset="utf-8">
<title>Briarwood Tavern</title>
<link rel="stylesheet" href="https://fonts.googleapis.com/css2?family=Courgette&family=Open+Sans:wght@400;600;700&family=Oswald:wght@400;500&display=swap">
<style>
:root{
  --red:#e8473f;
  --red-dark:#c9342d;
  --ink:#222222;
  --text:#777777;
  --light:#f4f4f4;
  --black:#0c0c0c;
  --footer:#2b2b2b;
  --footer-bottom:#1e1e1e;
  --white:#ffffff;
  --green:#7bbf3a;
  --purple:#7a5ec9;
  --pink:#e94b7b;
}
*{box-sizing:border-box;margin:0;padding:0}
html,body{width:1200px;height:2724px;overflow:hidden}
body{font-family:"Open Sans",Arial,sans-serif;color:var(--text);background:var(--white);font-size:15px;line-height:1.7}
.script{font-family:"Courgette",cursive;font-weight:400}

/* header */
.site-header{height:140px;position:relative;background:var(--white)}
.brand{position:absolute;left:100px;top:24px;display:flex;align-items:center;gap:12px}
.brand-dot{width:22px;height:22px;border-radius:50%;background:var(--red)}
.brand-name{font-family:"Oswald",sans-serif;font-size:28px;color:var(--ink);letter-spacing:1px}
.phone{position:absolute;right:100px;top:16px;display:flex;align-items:center;gap:8px;font-size:15px;color:var(--red)}
.main-nav{position:absolute;right:90px;top:58px;display:flex;gap:24px}
.main-nav a{font-family:"Oswald",sans-serif;font-size:15px;color:var(--ink);text-decoration:none;padding:8px 22px;letter-spacing:1px}
.main-nav a.active{border:2px solid var(--red);color:var(--red);border-radius:3px}

/* hero */
.hero{height:520px;position:relative;background:radial-gradient(ellipse at 60% 40%,#b8662a 0%,#7a3a14 45%,#2b1409 100%);display:flex;flex-direction:column;align-items:center;justify-content:center;text-align:center}
.hero-name{font-family:"Oswald",sans-serif;font-size:30px;color:var(--white);letter-spacing:3px;margin-top:-40px;display:flex;align-items:center;gap:12px}
.hero-name span.sq{width:18px;height:18px;background:var(--white)}
.hero-title{font-size:64px;color:var(--white);margin-top:50px;text-shadow:0 2px 8px rgba(0,0,0,.5)}

/* welcome */
.welcome{height:340px;position:relative;background:var(--white)}
.welcome-photo{position:absolute;left:200px;top:70px;width:240px;height:200px;border-radius:6px;background:linear-gradient(160deg,#d89a4a,#8a3f1c 55%,#4d6b22)}
.welcome-body{position:absolute;left:500px;top:70px;width:560px}
.section-title{font-size:30px;color:var(--ink)}
.welcome-body .section-title::after{content:"";display:block;width:520px;height:1px;background:#dddddd;margin-top:10px}
.welcome-body p{margin-top:16px;font-size:14px}
.btn{display:inline-block;background:var(--red);color:var(--white);font-family:"Oswald",sans-serif;font-size:14px;letter-spacing:1px;padding:8px 24px;border-radius:3px;text-decoration:none;margin-top:28px}

/* menu band */
.menu-band{height:420px;position:relative;background:var(--black)}
.menu-photo{position:absolute;left:0;top:0;width:580px;height:420px;background:radial-gradient(circle at 45% 45%,#e3b24a 0%,#b9731f 40%,#3a2410 75%,#0c0c0c 100%)}
.menu-body{position:absolute;left:680px;top:50px;width:420px;color:#cccccc}
.menu-body .section-title{color:var(--white)}
.menu-body p{margin-top:16px;font-size:14px}
.menu-list{list-style:none;margin-top:20px}
.menu-list li{display:flex;align-items:center;gap:14px;font-size:14px;padding:6px 0;border-bottom:1px solid #2a2a2a;color:#dddddd}
.color-strip{display:flex;justify-content:center;gap:10px;height:8px;margin-top:0}
.color-strip span{width:250px;height:8px}

/* features */
.features{height:300px;display:flex;justify-content:center;gap:40px;padding-top:40px}
.feature{width:230px;text-align:center}
.feature-icon{width:88px;height:88px;border-radius:50%;background:#333333;margin:0 auto;display:flex;align-items:center;justify-content:center}
.feature-icon.accent{background:var(--red)}
.feature h3{font-family:"Oswald",sans-serif;font-weight:500;font-size:18px;color:var(--ink);margin-top:16px;letter-spacing:1px}
.feature p{font-size:13px;margin-top:6px}
.feature .more{font-family:"Oswald",sans-serif;font-size:13px;color:var(--red);margin-top:6px;display:block;letter-spacing:1px}

/* gallery */
.gallery{height:452px;background:linear-gradient(180deg,#efe6dd,#d9c8b8);text-align:center;padding-top:60px}
.gallery .section-title{font-size:34px}
.gallery-grid{display:flex;justify-content:center;gap:14px;margin-top:36px}
.gallery-item{width:240px;height:200px;border:4px solid var(--white)}
.g1{background:linear-gradient(150deg,#e07b4a,#a0402a 60%,#6f8a3a)}
.g2{background:linear-gradient(150deg,#f0c45a,#c88a2a 60%,#7a4a1f)}
.g3{background:linear-gradient(150deg,#d2552a,#9a2f15 60%,#5a1a0d)}
.g4{background:linear-gradient(150deg,#e8a04a,#c0602a 60%,#8a3a1a)}

/* testimonials */
.testimonials{height:300px;position:relative;text-align:center;padding-top:16px}
.testimonials .section-title{font-size:32px}
.client-photo{position:absolute;left:160px;top:80px;width:180px;height:180px;border-radius:50%;background:linear-gradient(180deg,#f2f2f2,#d9d4cf)}
.quote{position:absolute;left:400px;top:100px;width:660px;text-align:left;font-size:14px;font-style:italic}
.quote-mark{position:absolute;font-family:Georgia,serif;font-size:60px;color:#cccccc;line-height:1}
.client-name{font-family:"Oswald",sans-serif;color:var(--red);font-size:14px;margin-top:14px;font-style:normal;letter-spacing:1px}
.client-role{font-size:13px;font-style:normal}

/* footer */
.site-footer{height:210px;background:var(--footer);display:flex;justify-content:center;gap:60px;padding-top:22px}
.footer-col{width:220px;color:#bbbbbb}
.footer-col h4{font-family:"Oswald",sans-serif;font-weight:500;color:var(--white);font-size:16px;letter-spacing:1px}
.footer-col ul{list-style:none;margin-top:10px}
.footer-col li{font-size:13px;line-height:1.65;display:flex;align-items:center;gap:8px}
.footer-col li::before{content:"";width:5px;height:5px;background:var(--red);border-radius:50%}
.field{height:26px;background:var(--white);border-radius:2px;margin-top:10px}
.subscribe{display:inline-block;background:var(--red);color:var(--white);font-family:"Oswald",sans-serif;font-size:12px;padding:3px 14px;margin-top:10px;border-radius:2px}
.footer-bottom{height:34px;background:var(--footer-bottom);display:flex;align-items:center;justify-content:space-between;padding:0 100px;font-size:12px;color:#999999}
.social{display:flex;gap:8px}
.social span{width:20px;height:20px;border-radius:50%;background:#888888}
</style>
</head>
<body>

<header class="site-header">
  <div class="brand"><span class="brand-dot"></span><span class="brand-name">BRIARWOOD TAVERN</span></div>
  <div class="phone">
    <svg width="16" height="16" viewBox="0 0 24 24"><path fill="#e8473f" d="M6.6 10.8a15.1 15.1 0 0 0 6.6 6.6l2.2-2.2a1 1 0 0 1 1-.25 11.4 11.4 0 0 0 3.6.57 1 1 0 0 1 1 1V20a1 1 0 0 1-1 1A17 17 0 0 1 3 4a1 1 0 0 1 1-1h3.5a1 1 0 0 1 1 1c0 1.25.2 2.45.57 3.57a1 1 0 0 1-.25 1z"/></svg>
    (555) 014-2290
  </div>
  <nav class="main-nav">
    <a class="active" href="#">HOME</a><a href="#">MENU</a><a href="#">EVENTS</a><a href="#">GALLERY</a><a href="#">CONTACT US</a>
  </nav>
</header>

<section class="hero" role="img" aria-label="Close-up of glazed chicken wings on a dark table">
  <div class="hero-name"><span class="sq"></span>BRIARWOOD TAVERN</div>
  <h1 class="hero-title script">Taste the Treasures of the Hollow</h1>
</section>

<section class="welcome">
  <div class="welcome-photo" role="img" aria-label="Burger with lettuce and tomato on a sesame bun"></div>
  <div class="welcome-body">
    <h2 class="section-title script">Welcome To Our Website</h2>
    <p>Our kitchen serves honest food made with local produce, paired with sixteen craft beers on tap and wines from nearby vineyards. Pull up a stool, meet the brewers and stay a while with friends old and new.</p>
    <a class="btn" href="#">READ MORE</a>
  </div>
</section>

<section class="menu-band">
  <div class="menu-photo" role="img" aria-label="Plate of fried rice with vegetables and chopsticks"></div>
  <div class="menu-body">
    <h2 class="section-title script">Our Latest Menu</h2>
    <p>Fresh dishes change with the season, built to match what is pouring from our taps tonight and ready for sharing.</p>
    <ul class="menu-list">
      <li><svg width="10" height="10" viewBox="0 0 10 10"><path d="M2 1l5 4-5 4" stroke="#e8473f" stroke-width="2" fill="none"/></svg>Smoked brisket sliders</li>
      <li><svg width="10" height="10" viewBox="0 0 10 10"><path d="M2 1l5 4-5 4" stroke="#e8473f" stroke-width="2" fill="none"/></svg>Beer battered fish</li>
      <li><svg width="10" height="10" viewBox="0 0 10 10"><path d="M2 1l5 4-5 4" stroke="#e8473f" stroke-width="2" fill="none"/></svg>Pub pretzel board</li>
      <li><svg width="10" height="10" viewBox="0 0 10 10"><path d="M2 1l5 4-5 4" stroke="#e8473f" stroke-width="2" fill="none"/></svg>House garden salad</li>
    </ul>
  </div>
</section>

<div class="color-strip"><span style="background:var(--green)"></span><span style="background:var(--red)"></span><span style="background:var(--pink)"></span><span style="background:var(--purple)"></span></div>

<section class="features">
  <div class="feature">
    <div class="feature-icon accent"><svg width="40" height="40" viewBox="0 0 40 40" fill="none" stroke="#fff" stroke-width="3"><path d="M12 6v28M8 6v8a4 4 0 0 0 8 0V6M28 6c-4 4-4 12 0 14v14"/></svg></div>
    <h3>NEW DISHES</h3><p>Seasonal plates fresh from our kitchen every week.</p><span class="more">VIEW MORE</span>
  </div>
  <div class="feature">
    <div class="feature-icon"><svg width="40" height="40" viewBox="0 0 40 40" fill="none" stroke="#fff" stroke-width="3"><path d="M9 12h18v16a6 6 0 0 1-6 6h-6a6 6 0 0 1-6-6zM27 16h3a4 4 0 0 1 0 8h-3"/></svg></div>
    <h3>DRINKS</h3><p>Sixteen craft beers on tap and local wines.</p><span class="more">VIEW MORE</span>
  </div>
  <div class="feature">
    <div class="feature-icon"><svg width="40" height="40" viewBox="0 0 40 40" fill="none" stroke="#fff" stroke-width="3"><path d="M20 5l4.5 9.5 10 1.3-7.3 7 1.9 10L20 28l-9.1 4.8 1.9-10-7.3-7 10-1.3z"/></svg></div>
    <h3>POPULAR</h3><p>The favourites our regulars order again and again.</p><span class="more">VIEW MORE</span>
  </div>
  <div class="feature">
    <div class="feature-icon"><svg width="40" height="40" viewBox="0 0 40 40" fill="none" stroke="#fff" stroke-width="3"><path d="M6 6h14l14 14-14 14L6 20z"/><circle cx="13" cy="13" r="2"/></svg></div>
    <h3>SPEAL OFFERS</h3><p>Weekly deals and happy hour pints for everyone.</p><span class="more">VIEW MORE</span>
  </div>
</section>

<section class="gallery">
  <h2 class="section-title script">Our Latest Gallery</h2>
  <div class="gallery-grid">
    <div class="gallery-item g1" role="img" aria-label="Grilled salmon with vegetables"></div>
    <div class="gallery-item g2" role="img" aria-label="Bowl of pasta with herbs"></div>
    <div class="gallery-item g3" role="img" aria-label="Spicy curry in a dish"></div>
    <div class="gallery-item g4" role="img" aria-label="Assorted shared plates on a table"></div>
  </div>
</section>

<section class="testimonials">
  <h2 class="section-title script">Testimonials</h2>
  <div class="client-photo" role="img" aria-label="Portrait of a chef in a white hat"></div>
  <div class="quote">
    <span class="quote-mark" style="left:-34px;top:-14px">&ldquo;</span>
    Great beer, warm service and a kitchen that clearly cares. We stopped in on a weekend trip and ended up staying all evening, working our way through the taps and the snack menu. The staff knew every brew by heart and made us feel like locals. Already planning our next visit.
    <span class="quote-mark" style="right:-30px;bottom:-30px">&rdquo;</span>
    <div class="client-name">ELLIS HART</div>
    <div class="client-role">Head Cook</div>
  </div>
</section>

<footer>
  <div class="site-footer">
    <div class="footer-col"><h4>WELCOME</h4><ul><li>Home</li><li>Menu</li><li>Events</li><li>Gallery</li><li>Contact Us</li></ul></div>
    <div class="footer-col"><h4>INFORMATION</h4><ul><li>Press Kit</li><li>Careers</li><li>Contact Us</li><li>Privacy</li><li>Return Us</li><li>Overview</li></ul></div>
    <div class="footer-col"><h4>SUPPORT LINKS</h4><ul><li>Latest Brews</li><li>Tap List</li><li>Wine Menu</li><li>Industry</li></ul></div>
    <div class="footer-col"><h4>SIGN UP NEWSLETTER</h4><div class="field"></div><div class="field"></div><span class="subscribe">SUBMIT</span></div>
  </div>
  <div class="footer-bottom">
    <span>&copy;2015 BriarwoodTavern.example All Rights Reserved</span>
    <div class="social"><span></span><span></span><span></span><span></span><span></span></div>
  </div>
</footer>

</body>
</html>
```